Business Card Design - Brightfold Dwellings

Hi there,

We would like a business card for our new venture, Brightfold Dwellings.

We are based in Western Australia and specialise in taking tired, old properties and making them look new again. We aim to create enjoyably liveable homes for young families in particular.

Product pricing is mid range i.e. appliances, furnishings, fixtures (not top end but not cheap either)

Our work is primarily cosmetic renovation (approx. 80%) and the rest construction (approx 20%).

We would like a business card that conveys the following:
- clean, simplistic/minimalistic design
- modern, contemporary style
- a touch of funk/uniqueness
- appealing to both females and males
- professionalism

I have uploaded our logo in grey or green, I do not mind which one you choose to use (please use either coloured logo on the pure white background not the white on colour version).

Details to include on the business card are:
Names: Corina Maddox and Pete Okonbrie
Mobile: 0417 362 908
Email: info@brightfolddwellings.com.au
Website: www.brightfolddwellings.com.au (note: this website is currently being developed)
Note: We will provide final details such as mobile number and names on on selection of successful design)

On the other side of the card please include a line similar to "We buy tired, un-renovated properties and sell them looking new again!"

The business card will also need to include the following "ABN 47 219 635 104" which is our Australian Business Number (again the actual number will be provided on selection of successful design). We would like this number somewhere near our name Brightfold Dwellings but in much smaller text.

The purpose of the business cards will be to give to suppliers, real estate agents, people wanting assistance in locating a property in need of renovation and potential buyers.

Thank you and please let me know if you have any further questions.

```html
<!DOCTYPE html>
<html lang="en">
<head>
<meta charset="utf-8">
<title>Brightfold Dwellings – Business Card</title>
<link href="https://fonts.googleapis.com/css2?family=Open+Sans:wght@300;400;600&display=swap" rel="stylesheet">
<style>
  :root {
    --lime: #8dc63f;
    --lime-light: #b5dc57;
    --lime-dark: #6fae22;
    --charcoal: #2e2e2e;
    --grey: #8a8a8a;
    --grey-light: #d9d9d9;
    --paper: #ffffff;
    --stage: #ece8e1;
    --ink: #3a3a3a;
  }
  html, body {
    margin: 0;
    padding: 0;
    width: 704px;
    height: 1200px;
    overflow: hidden;
    background: var(--stage);
    font-family: "Open Sans", Arial, sans-serif;
  }
  .canvas { position: relative; width: 704px; height: 1200px; }
  .card {
    position: absolute;
    left: 72px;
    width: 560px;
    height: 320px;
    border-radius: 16px;
    overflow: hidden;
    box-shadow: 0 6px 18px rgba(0,0,0,0.18);
  }
  .card--front { top: 120px; background: var(--paper); }
  .card--back {
    top: 760px;
    background: linear-gradient(160deg, var(--lime-light) 0%, var(--lime) 55%, var(--lime-dark) 100%);
  }
  .card__waves { position: absolute; inset: 0; width: 560px; height: 320px; }

  .brand {
    position: absolute;
    display: flex;
    align-items: center;
    gap: 12px;
    white-space: nowrap;
  }
  .brand__mark { flex: none; border-radius: 50%; }
  .brand__name { margin: 0; font-weight: 400; letter-spacing: -0.5px; }

  .card--front .brand { left: 40px; top: 106px; }
  .card--front .brand__mark { width: 22px; height: 22px; background: var(--lime); }
  .card--front .brand__name { font-size: 30px; color: var(--lime); }

  .brand-rule {
    position: absolute;
    left: 40px;
    top: 158px;
    width: 330px;
    height: 4px;
    background: var(--grey-light);
  }
  .brand-rule::before {
    content: "";
    position: absolute;
    left: 0;
    top: -1px;
    width: 150px;
    height: 6px;
    background: var(--lime);
  }
  .abn {
    position: absolute;
    left: 40px;
    top: 168px;
    margin: 0;
    font-size: 9px;
    letter-spacing: 0.4px;
    color: var(--grey);
  }
  .contact-list {
    position: absolute;
    left: 40px;
    top: 196px;
    margin: 0;
    padding: 0;
    list-style: none;
    font-size: 13px;
    color: var(--ink);
    line-height: 22px;
  }
  .contact-list li { display: flex; align-items: center; gap: 10px; }
  .contact-list svg { width: 11px; height: 11px; flex: none; }

  .person { position: absolute; right: 128px; top: 34px; text-align: right; }
  .person__name { margin: 0; font-size: 16px; font-weight: 400; color: var(--lime); }
  .person__role {
    margin: 2px 0 0;
    font-size: 12px;
    color: var(--charcoal);
    padding-bottom: 6px;
    border-bottom: 5px solid var(--charcoal);
    min-width: 120px;
    text-align: left;
  }

  .card--back .brand { left: 44px; top: 118px; }
  .card--back .brand__mark { width: 26px; height: 26px; border: 3px solid var(--paper); box-sizing: border-box; }
  .card--back .brand__name { font-size: 34px; font-weight: 300; color: var(--paper); }
  .tagline {
    position: absolute;
    left: 44px;
    top: 176px;
    width: 330px;
    margin: 0;
    font-size: 13px;
    line-height: 19px;
    color: var(--paper);
  }
</style>
</head>
<body>
<main class="canvas">

  <section class="card card--front" aria-label="Business card front">
    <svg class="card__waves" viewBox="0 0 560 320" aria-hidden="true">
      <path d="M560 0 L520 0 C440 90 560 210 430 320 L560 320 Z" fill="#d6d6d6"/>
      <path d="M560 0 L540 0 C470 100 580 220 465 320 L560 320 Z" fill="#5a5a5a"/>
      <path d="M560 40 C500 130 600 230 500 320 L560 320 Z" fill="#262626"/>
      <path d="M505 0 C425 90 540 210 410 320" fill="none" stroke="#8dc63f" stroke-width="3"/>
    </svg>

    <div class="person">
      <p class="person__name">Corina Maddox</p>
      <p class="person__role">Designation</p>
    </div>

    <div class="brand">
      <span class="brand__mark"></span>
      <h1 class="brand__name">Brightfold Dwellings</h1>
    </div>
    <div class="brand-rule"></div>
    <p class="abn">ABN 47 219 635 104</p>

    <ul class="contact-list">
      <li>
        <svg viewBox="0 0 12 12"><rect x="1" y="1" width="10" height="10" rx="1" fill="none" stroke="#8a8a8a" stroke-width="1.2"/></svg>
        0417 362 908
      </li>
      <li>
        <svg viewBox="0 0 12 12"><rect x="1" y="2" width="10" height="8" fill="#8dc63f"/></svg>
        info@brightfolddwellings.com.au
      </li>
      <li>
        <svg viewBox="0 0 12 12"><circle cx="6" cy="6" r="5" fill="none" stroke="#8a8a8a" stroke-width="1.2"/></svg>
        www.brightfolddwellings.com.au
      </li>
    </ul>
  </section>

  <section class="card card--back" aria-label="Business card back">
    <svg class="card__waves" viewBox="0 0 560 320" aria-hidden="true">
      <path d="M560 0 L470 0 C400 80 430 230 250 320 L560 320 Z" fill="#2b2b2b"/>
      <path d="M560 0 L495 0 C425 90 455 235 295 320 L560 320 Z" fill="#ffffff"/>
      <path d="M560 0 L520 0 C450 100 480 240 340 320 L560 320 Z" fill="#9a9a9a"/>
      <path d="M560 0 L545 0 C478 110 505 245 385 320 L560 320 Z" fill="#f1f1f1"/>
    </svg>
    <div class="brand">
      <span class="brand__mark"></span>
      <h2 class="brand__name">Brightfold Dwellings</h2>
    </div>
    <p class="tagline">We buy tired, un-renovated properties and sell them looking new again!</p>
  </section>

</main>
</body>
</html>
```